Inspire Design with Natural Stone: Quarrell Ltd. Tradeshow Booth Backdrop

Client: Quarrell Ltd.
Project Goal: To design a visually compelling and informative 7.5ft x 10ft backdrop for Quarrell Ltd.'s 10ft x 10ft tradeshow booth that attracts and engages architects, designers, homeowners, and contractors, ultimately driving interest in their natural stone products.
Quarrell Ltd. is a leading provider of high-quality natural stone for a wide range of residential and commercial projects. We offer a diverse selection of stone types, finishes, and applications, known for their beauty, durability, and timeless appeal. We are participating in upcoming tradeshows to generate new leads, strengthen brand awareness, and showcase our latest offerings to key target audiences.
Target Audience(s):
Architects: Seeking premium, unique, and sustainable natural stone options for their designs, with an appreciation for quality and aesthetic integration.
Designers (Interior & Landscape): Looking for visually appealing and versatile stone to enhance their projects, focusing on texture, color palettes, and application possibilities.
Homeowners: Aspiring to elevate their living spaces with natural stone, driven by aesthetics, durability, and adding lasting value to their homes.
Contractors: Seeking reliable and high-quality stone suppliers for their building and renovation projects, prioritizing ease of installation and client satisfaction.
Key Message/Desired Outcome: We want our booth to communicate that Quarrell Ltd. is the premier source for beautiful, high-quality natural stone solutions for any project, backed by expertise and a commitment to customer satisfaction. We want to inspire visitors with the possibilities of using natural stone in their designs and projects.
Mandatories:
* Backdrop Dimensions: 7.5 feet (height) x 10 feet (width). (See attached template)
* Inclusion of Quarrell Ltd. Logo:* The logo must be prominently featured and easily recognizable. Please refer to the attached brand guidelines for logo usage, color palette, and typography.
*Clear Representation of Natural Stone: The design must showcase the beauty and variety of Quarrell Ltd.'s natural stone products. This can be achieved through high-quality photography, subtle textures, or artistic representations. Please use our website's photo and project gallery.
*Contact Information: Include our website address: www.quarrellbrix.example
Optional Elements (Consideration):
*Visuals of Applications: Showcasing natural stone used in various settings (e.g., fireplaces, facades, patios, interior walls) could be impactful.
*Highlighting Key Benefits: Briefly communicating the advantages of natural stone (e.g., durability, sustainability, timelessness).
*Integration of Textures: Subtly incorporating textures that hint at the feel of natural stone.
Look and Feel:
*Overall Impression: Sophisticated, natural, high-quality, inviting, trustworthy, and inspiring.
*Style: Clean, modern, and visually appealing, allowing the beauty of the stone to take center stage. Avoid overly busy or cluttered designs.
*Color Palette: Primarily utilize Quarrell Ltd.'s brand colors (refer to brand guidelines).
Things to Avoid:
* Generic stock imagery that doesn't accurately represent Quarrell's products.
* Cluttered layouts with excessive text.
* Designs that appear cheap or unprofessional.
* Difficult-to-read fonts or color combinations.
Deliverables:
* High-resolution digital design file(s) suitable for large-format printing (AI, Photoshop, PDF).
* Mockup of the backdrop design within a 10ft x 10ft booth space. Please feel free to include any other booth features (tables, flooring, etc) that you think would work well with the backdrop (optional but highly recommended).
We are excited to see your creative interpretations and look forward to selecting a design that will make a strong and lasting impression at our upcoming tradeshows!

```html
<!DOCTYPE html>
<html lang="en">
<head>
<meta charset="utf-8">
<title>Quarrell Ltd. Tradeshow Backdrop</title>
<link rel="stylesheet" href="https://fonts.googleapis.com/css2?family=Exo+2:wght@300;400;500;600;700&display=swap">
<style>
  :root {
    --page-bg: #e4e4e4;
    --navy: #0f1d2e;
    --navy-deep: #0b1624;
    --beige: #cfc6a7;
    --grey-band: #7c7f84;
    --white: #ffffff;
    --line: #dfe3ea;
    --url-grey: #b9bcc2;
  }
  html, body {
    margin: 0;
    padding: 0;
    width: 1200px;
    height: 2179px;
    overflow: hidden;
    background: var(--page-bg);
    font-family: "Exo 2", sans-serif;
  }
  .backdrop {
    position: absolute;
    left: 50px;
    top: 677px;
    width: 1100px;
    height: 825px;
    background: radial-gradient(ellipse at 35% 25%, #14243a 0%, var(--navy) 55%, var(--navy-deep) 100%);
    box-shadow: 8px 10px 22px rgba(0,0,0,0.35);
    overflow: hidden;
  }
  .headline {
    position: absolute;
    right: 666px;
    top: 76px;
    margin: 0;
    text-align: right;
    font-weight: 400;
    line-height: 1;
  }
  .headline .lead {
    display: block;
    color: var(--white);
    font-size: 36px;
    font-weight: 400;
  }
  .headline .main {
    display: block;
    color: var(--beige);
    font-size: 50px;
    font-weight: 600;
    margin-top: 6px;
    letter-spacing: 0.5px;
  }
  .intro {
    position: absolute;
    right: 668px;
    top: 176px;
    width: 400px;
    margin: 0;
    text-align: right;
    color: var(--white);
    font-size: 15.5px;
    line-height: 19px;
  }
  .frame-line { position: absolute; background: var(--line); }
  .photo { position: absolute; }
  .photo-fireplace-stone { left: 674px; top: 99px; width: 230px; height: 323px;
    background: linear-gradient(180deg, #8a7660 0%, #a59a86 40%, #7a6a58 70%, #5b3b22 100%); }
  .photo-fireplace-slate { left: 202px; top: 269px; width: 229px; height: 322px;
    background: linear-gradient(90deg, #d9d8d4 0%, #c9c6bf 45%, #4e4f52 55%, #3c3d40 80%, #8e7a62 100%); }
  .photo-garden-wall { left: 438px; top: 363px; width: 230px; height: 322px;
    background: linear-gradient(180deg, #5c7148 0%, #6f8355 40%, #a9a190 65%, #3a3a3a 100%); }
  .brand-name {
    position: absolute;
    left: 452px;
    top: 282px;
    width: 200px;
    text-align: center;
    color: var(--white);
    font-size: 30px;
    font-weight: 500;
    margin: 0;
  }
  .offer-title {
    position: absolute;
    left: 689px;
    top: 450px;
    margin: 0;
    color: var(--white);
    font-size: 17.5px;
    font-weight: 600;
    line-height: 21px;
  }
  .offer-list {
    position: absolute;
    left: 675px;
    top: 504px;
    width: 245px;
    margin: 0;
    padding: 0;
    list-style: none;
  }
  .offer-list li {
    height: 29px;
    margin-bottom: 1.8px;
    display: flex;
    align-items: center;
    padding-left: 19px;
    color: var(--navy);
    font-size: 17px;
    font-weight: 400;
  }
  .offer-list li:nth-child(odd) { background: var(--beige); }
  .offer-list li:nth-child(even) { background: var(--grey-band); }
  .tick { width: 13px; height: 13px; margin-right: 9px; flex: none; }
  .website {
    position: absolute;
    left: 0;
    width: 1100px;
    top: 726px;
    margin: 0;
    text-align: center;
    font-size: 23px;
    letter-spacing: 9px;
    color: var(--url-grey);
    font-weight: 300;
  }
  .website .domain { color: var(--beige); font-weight: 700; }
</style>
</head>
<body>
  <main class="backdrop">
    <h1 class="headline">
      <span class="lead">CRAFT YOUR</span>
      <span class="main">VISION IN STONE</span>
    </h1>
    <p class="intro">Quarrell Ltd. is a leading provider of high-quality natural stone for a wide range of residential and commercial projects.</p>

    <div class="frame-line" style="left:449px; top:80px; width:472px; height:2px;"></div>
    <div class="frame-line" style="left:919px; top:80px; width:2px; height:232px;"></div>
    <div class="frame-line" style="left:904px; top:310px; width:17px; height:2px;"></div>

    <div class="frame-line" style="left:186px; top:377px; width:2px; height:232px;"></div>
    <div class="frame-line" style="left:186px; top:607px; width:230px; height:2px;"></div>
    <div class="frame-line" style="left:186px; top:377px; width:16px; height:2px;"></div>

    <div class="photo photo-fireplace-stone" role="img" aria-label="Photo of a tall natural fieldstone fireplace with a wooden mantel in a timber-ceiling room"></div>
    <div class="photo photo-fireplace-slate" role="img" aria-label="Photo of a dark slate stone fireplace chimney in a bright living room"></div>
    <div class="photo photo-garden-wall" role="img" aria-label="Photo of a dry-laid stone garden wall in front of trees and a house"></div>

    <p class="brand-name">Quarrell Ltd.</p>

    <h2 class="offer-title">We offer a diverse<br>selection of</h2>
    <ul class="offer-list">
      <li><svg class="tick" viewBox="0 0 14 14"><circle cx="7" cy="7" r="7" fill="#0f1d2e"/><path d="M3.8 7.2 L6 9.3 L10.2 4.9" stroke="#cfc6a7" stroke-width="1.8" fill="none"/></svg>Stone types</li>
      <li><svg class="tick" viewBox="0 0 14 14"><circle cx="7" cy="7" r="7" fill="#0f1d2e"/><path d="M3.8 7.2 L6 9.3 L10.2 4.9" stroke="#7c7f84" stroke-width="1.8" fill="none"/></svg>Finishes</li>
      <li><svg class="tick" viewBox="0 0 14 14"><circle cx="7" cy="7" r="7" fill="#0f1d2e"/><path d="M3.8 7.2 L6 9.3 L10.2 4.9" stroke="#cfc6a7" stroke-width="1.8" fill="none"/></svg>Applications</li>
      <li><svg class="tick" viewBox="0 0 14 14"><circle cx="7" cy="7" r="7" fill="#0f1d2e"/><path d="M3.8 7.2 L6 9.3 L10.2 4.9" stroke="#7c7f84" stroke-width="1.8" fill="none"/></svg>Known for their beauty</li>
      <li><svg class="tick" viewBox="0 0 14 14"><circle cx="7" cy="7" r="7" fill="#0f1d2e"/><path d="M3.8 7.2 L6 9.3 L10.2 4.9" stroke="#cfc6a7" stroke-width="1.8" fill="none"/></svg>Durability</li>
      <li><svg class="tick" viewBox="0 0 14 14"><circle cx="7" cy="7" r="7" fill="#0f1d2e"/><path d="M3.8 7.2 L6 9.3 L10.2 4.9" stroke="#7c7f84" stroke-width="1.8" fill="none"/></svg>Timeless appeal</li>
    </ul>

    <p class="website">www.<span class="domain">quarrellbrix</span>.example</p>
  </main>
</body>
</html>
```